Tovane and Partners Business Card

A business card that can be templates for all employees using our newly created logo and information. We are looking for stylish however simplistic in nature, clean looks are better than over the top, however creativity will be appreciated if it has the right appeal. Note: If you feel a type of card (plastic, metalic, carbon, raised lettering, etc) helps your design please specify.
Target Market(s)
Investigation ETC
Industry/Entity Type
Private Investigator
Contact Information for Business Card
Dan Moskel
President
5173 Wexmoor Lane
Brenford OH 43910-2257
Cell: 555-555-0193; Office: 555-555-0147
Email: danmoskel@tovanepartners-example.com
Requirements
Must have
- Website TovanePartners-example.com
- Name, address, phone number ETC
- Use of current Logo and color pallets if applicable
- TM By logo, small

Nice to have
- Would like to see with and without a photo on the design

Should not have
- Redesign of logo, changing of colors

```html
<!DOCTYPE html>
<html lang="en">
<head>
<meta charset="utf-8">
<title>Tovane and Partners – Business Card</title>
<link rel="stylesheet" href="https://fonts.googleapis.com/css2?family=Open+Sans:wght@400;600;700&family=Montserrat:wght@800&display=swap">
<style>
  :root {
    --bg: #e9e6e1;
    --card-white: #f7f7f7;
    --card-black: #111111;
    --orange: #f07a1a;
    --orange-light: #f6a733;
    --red-orange: #e2451d;
    --grey-text: #555555;
    --grey-dark: #6a6a6a;
    --white: #ffffff;
  }
  * { margin: 0; padding: 0; box-sizing: border-box; }
  html, body { width: 1200px; height: 780px; overflow: hidden; background: var(--bg); }
  .canvas { position: relative; width: 1200px; height: 780px; }

  .card {
    position: absolute; top: 235px; width: 540px; height: 309px;
    box-shadow: 0 6px 18px rgba(0,0,0,.18); overflow: hidden;
  }
  .card--front { left: 40px; background: var(--card-white); }
  .card--back { left: 620px; background: var(--card-black); }

  .front__band { position: absolute; left: 0; top: 0; width: 540px; height: 309px; }

  .front__brand {
    position: absolute; left: 38px; top: 70px;
    display: flex; align-items: center; gap: 12px;
  }
  .brand__mark { width: 14px; height: 14px; border-radius: 50%; background: var(--red-orange); }
  .brand__name {
    font-family: "Montserrat", sans-serif; font-weight: 800; font-size: 27px;
    letter-spacing: .5px; color: var(--red-orange); text-transform: uppercase; line-height: 1;
  }

  .front__person { position: absolute; left: 40px; top: 126px; font-family: "Open Sans", sans-serif; }
  .person__name { font-weight: 700; font-size: 21px; color: var(--grey-dark); line-height: 1.1; }
  .person__title { font-weight: 600; font-size: 14px; color: var(--red-orange); }

  .front__contact {
    position: absolute; left: 236px; top: 180px; list-style: none;
    font-family: "Open Sans", sans-serif; font-size: 12px; color: var(--grey-text);
  }
  .contact__item { display: flex; align-items: center; gap: 8px; height: 20px; white-space: nowrap; }
  .contact__icon {
    width: 14px; height: 14px; background: var(--orange); border-radius: 2px;
    display: flex; align-items: center; justify-content: center;
  }
  .contact__icon svg { width: 10px; height: 10px; }
  .contact__item--plain { padding-left: 22px; }

  .back__brand {
    position: absolute; inset: 0;
    display: flex; align-items: center; justify-content: center; gap: 14px;
  }
  .back__brand .brand__mark { background: var(--white); width: 16px; height: 16px; }
  .back__brand .brand__name { color: var(--white); font-size: 30px; }
</style>
</head>
<body>
<main class="canvas">

  <section class="card card--front" aria-label="Business card front">
    <svg class="front__band" viewBox="0 0 540 309" aria-hidden="true">
      <defs>
        <linearGradient id="bandFill" x1="0" y1="0" x2="1" y2="0">
          <stop offset="0" stop-color="#ee6a12"/>
          <stop offset="1" stop-color="#f6a733"/>
        </linearGradient>
      </defs>
      <path d="M0 178 L180 178 Q195 178 200 192 L228 309 L0 309 Z" fill="url(#bandFill)"/>
      <path d="M0 178 L180 178 Q195 178 200 192 L228 309" fill="none" stroke="#ffffff" stroke-width="2"/>
    </svg>

    <div class="front__brand">
      <span class="brand__mark"></span>
      <span class="brand__name">Tovane and Partners</span>
    </div>

    <div class="front__person">
      <p class="person__name">Dan Moskel</p>
      <p class="person__title">President</p>
    </div>

    <ul class="front__contact">
      <li class="contact__item">
        <span class="contact__icon"><svg viewBox="0 0 10 10"><rect x="3" y="1" width="4" height="8" rx="1" fill="none" stroke="#fff" stroke-width="1"/></svg></span>
        555-555-0193
      </li>
      <li class="contact__item">
        <span class="contact__icon"><svg viewBox="0 0 10 10"><path d="M2 1 L4 3 L3 4 Q4 6 6 7 L7 6 L9 8 L8 9 Q3 9 1 2 Z" fill="#fff"/></svg></span>
        555-555-0147
      </li>
      <li class="contact__item">
        <span class="contact__icon"><svg viewBox="0 0 10 10"><rect x="1" y="2" width="8" height="6" fill="none" stroke="#fff" stroke-width="1"/><path d="M1 2 L5 5.5 L9 2" fill="none" stroke="#fff" stroke-width="1"/></svg></span>
        danmoskel@tovanepartners-example.com
      </li>
      <li class="contact__item">
        <span class="contact__icon"><svg viewBox="0 0 10 10"><circle cx="5" cy="5" r="3.8" fill="none" stroke="#fff" stroke-width="1"/><path d="M1.2 5 H8.8 M5 1.2 Q2.5 5 5 8.8 Q7.5 5 5 1.2" fill="none" stroke="#fff" stroke-width=".8"/></svg></span>
        TovanePartners-example.com
      </li>
      <li class="contact__item contact__item--plain">5173 Wexmoor Lane Brenford OH 43910-2257</li>
    </ul>
  </section>

  <section class="card card--back" aria-label="Business card back">
    <div class="back__brand">
      <span class="brand__mark"></span>
      <span class="brand__name">Tovane and Partners</span>
    </div>
  </section>

</main>
</body>
</html>
```